Design a business card
Business name: Kestrel Yield Consulting
Improving Business Profitibility

- An Overview of the Business & Service:

Business Performance Consulting

- The Target Market: Small to medium-sized business

- Design Specifics:
White card, blue ink, moon eclipse

No Logo

Target Market(s)

Small to medium-sized business

Font styles to use
Sans Serif

```html
<!DOCTYPE html>
<html lang="en">
<head>
<meta charset="utf-8">
<title>Kestrel Yield Consulting – Business Card</title>
<link rel="stylesheet" href="https://fonts.googleapis.com/css2?family=Open+Sans:wght@400;600;700&display=swap">
<style>
  :root {
    --backdrop: #e6e7ea;
    --card-white: #ffffff;
    --brand-blue: #1155c4;
    --title-blue: #1a62c9;
    --accent-cyan: #22c3f0;
    --ink-dark: #1c1c28;
    --tagline-white: #ffffff;
  }
  * { box-sizing: border-box; margin: 0; padding: 0; }
  html, body {
    width: 1200px; height: 977px; overflow: hidden;
    background: var(--backdrop);
    font-family: "Open Sans", Arial, sans-serif;
  }
  .business-card {
    position: absolute; left: 150px; top: 231px;
    width: 900px; height: 514px;
    background: var(--card-white);
    overflow: hidden;
    box-shadow: 0 10px 30px rgba(0,0,0,0.18);
  }
  .card-waves { position: absolute; inset: 0; }
  .company-name {
    position: absolute; right: 42px; top: 28px;
    font-weight: 700; font-size: 38px; letter-spacing: 0.5px;
    color: var(--title-blue); text-transform: uppercase; white-space: nowrap;
  }
  .person {
    position: absolute; right: 390px; top: 150px; text-align: right;
  }
  .person-name { font-size: 29px; color: var(--title-blue); font-weight: 400; line-height: 1.1; white-space: nowrap; }
  .person-title { font-size: 15px; color: var(--ink-dark); font-weight: 600; margin-top: 2px; }
  .divider {
    position: absolute; left: 528px; top: 126px;
    width: 2px; height: 106px; background: var(--ink-dark);
  }
  .contact {
    position: absolute; left: 548px; top: 116px;
    font-size: 14px; font-style: normal; color: var(--ink-dark); line-height: 1.25;
  }
  .contact-address { margin-bottom: 8px; white-space: nowrap; }
  .contact-row { display: flex; align-items: center; gap: 11px; margin-bottom: 3px; white-space: nowrap; }
  .contact-icon { width: 13px; height: 13px; flex: none; fill: var(--brand-blue); }
  .tagline {
    position: absolute; left: 0; right: 0; bottom: 30px; text-align: center;
    color: var(--tagline-white); font-size: 29px; font-weight: 600;
    letter-spacing: 5px; text-transform: uppercase; white-space: nowrap;
  }
</style>
</head>
<body>
  <main class="business-card">
    <svg class="card-waves" viewBox="0 0 900 514" width="900" height="514" aria-hidden="true">
      <path fill="var(--brand-blue)" d="M0,320 C350,380 780,330 900,110 L900,514 L0,514 Z"/>
      <path fill="var(--accent-cyan)" d="M40,298 C350,358 770,306 892,92 C780,326 350,374 40,298 Z"/>
    </svg>

    <h1 class="company-name">Kestrel Yield Consulting</h1>

    <div class="person">
      <p class="person-name">Desmond R Hale</p>
      <p class="person-title">President</p>
    </div>

    <div class="divider"></div>

    <address class="contact">
      <p class="contact-address">Alder Lane Station<br>PO Box 418, Fairhaven</p>
      <p class="contact-row">
        <svg class="contact-icon" viewBox="0 0 24 24"><path d="M6.6 10.8a15.1 15.1 0 0 0 6.6 6.6l2.2-2.2c.3-.3.7-.4 1-.2 1.1.4 2.3.6 3.6.6.6 0 1 .4 1 1V20c0 .6-.4 1-1 1A17 17 0 0 1 3 4c0-.6.4-1 1-1h3.5c.6 0 1 .4 1 1 0 1.3.2 2.5.6 3.6.1.3 0 .7-.2 1z"/></svg>
        555 014 2286
      </p>
      <p class="contact-row">
        <svg class="contact-icon" viewBox="0 0 24 24"><path d="M2 5h20v14H2z"/><path d="M3 6l9 7 9-7" fill="none" stroke="#fff" stroke-width="1.6"/></svg>
        info@kestrelyield.com
      </p>
      <p class="contact-row">
        <svg class="contact-icon" viewBox="0 0 24 24"><circle cx="12" cy="12" r="10"/><path d="M2 12h20M12 2c3 3 3 17 0 20M12 2c-3 3-3 17 0 20" fill="none" stroke="#fff" stroke-width="1.5"/></svg>
        www.kestrelyield.com
      </p>
    </address>

    <p class="tagline">Improving Business Profitibility</p>
  </main>
</body>
</html>
```